Relaxation, deep tissue sports massage

We need an opening of anew massage centre poster
relaxation, deep tissue and sports massage
POSTER SIZE A4 and for a 1meter X 1meter stand
the business name is Sorevo , we have a logo already , which i enclose
the poster needs to be eye catching
location Brinkley Lane Medical Clinic 0882719064 for an appointment
location uHealth on Torvale 0886217359 for an appointment

Target Market(s)

public

Industry/Entity Type

Massage

Requirements
Must have
• logo , be vibrant ,eye catching and inviting
Nice to have
• massage picture , logo etc

```html
<!DOCTYPE html>
<html lang="en">
<head>
<meta charset="utf-8">
<title>Sorevo massage – Relax Renew Revive</title>
<link rel="stylesheet" href="https://fonts.googleapis.com/css2?family=Oswald:wght@300;400&display=swap">
<style>
  :root {
    --leaf: #9ccc3c;
    --sky: #2bb4e8;
    --ink: #4a4a4a;
    --paper: #ffffff;
    --helmet: #2e2f36;
    --skin: #e9ac86;
    --skin-deep: #c87a55;
    --towel: #f6f0eb;
  }
  html, body {
    margin: 0;
    padding: 0;
    width: 873px;
    height: 1200px;
    overflow: hidden;
    background: var(--paper);
  }
  .poster {
    position: relative;
    width: 873px;
    height: 1200px;
    overflow: hidden;
    background: var(--paper);
    font-family: "Oswald", "Arial Narrow", sans-serif;
  }
  .artwork {
    position: absolute;
    inset: 0;
  }
  .brand {
    position: absolute;
    top: 150px;
    left: 0;
    width: 873px;
    text-align: center;
  }
  .brand-name {
    margin: 0;
    font-weight: 400;
    font-size: 66px;
    line-height: 1;
    color: var(--sky);
    letter-spacing: 1px;
  }
  .brand-tagline {
    margin: 14px 0 0;
    font-weight: 300;
    font-size: 25px;
    letter-spacing: 2px;
    color: var(--ink);
  }
  .contacts {
    position: absolute;
    top: 386px;
    left: 87px;
    display: flex;
    align-items: flex-start;
  }
  .phone-icon {
    width: 44px;
    height: 78px;
    margin-top: 16px;
    margin-right: 30px;
  }
  .location {
    border-left: 3px solid var(--leaf);
    padding-left: 13px;
    height: 112px;
    width: 318px;
  }
  .location + .location {
    width: 300px;
  }
  .location-phone {
    margin: 0;
    font-weight: 300;
    font-size: 48px;
    line-height: 56px;
    color: var(--leaf);
  }
  .location-detail {
    margin: 2px 0 0;
    font-weight: 300;
    font-size: 21px;
    line-height: 27px;
    color: var(--sky);
  }
  .services {
    position: absolute;
    left: 500px;
    top: 1034px;
    margin: 0;
    color: var(--paper);
    font-weight: 400;
    line-height: 1;
    text-shadow: 0 2px 4px rgba(0, 0, 0, 0.35);
  }
  .services-line {
    display: block;
    font-size: 38px;
  }
  .services-line--lead {
    font-size: 46px;
    margin-left: 30px;
  }
</style>
</head>
<body>
<main class="poster">
  <svg class="artwork" width="873" height="1200" viewBox="0 0 873 1200">
    <defs>
      <radialGradient id="photo-tone" cx="0.3" cy="0.38" r="0.75">
        <stop offset="0" stop-color="var(--helmet)"/>
        <stop offset="0.28" stop-color="#6b5248"/>
        <stop offset="0.48" stop-color="var(--skin-deep)"/>
        <stop offset="0.75" stop-color="var(--skin)"/>
        <stop offset="1" stop-color="#f2d2bd"/>
      </radialGradient>
      <linearGradient id="photo-fade" x1="0" y1="0" x2="0" y2="1">
        <stop offset="0" stop-color="#ffffff" stop-opacity="1"/>
        <stop offset="0.2" stop-color="#ffffff" stop-opacity="0"/>
        <stop offset="0.78" stop-color="var(--towel)" stop-opacity="0"/>
        <stop offset="0.92" stop-color="var(--towel)" stop-opacity="0.9"/>
        <stop offset="1" stop-color="var(--towel)"/>
      </linearGradient>
    </defs>
    <path class="band-top" d="M0 66 Q160 12 333 0 L262 0 Q110 16 0 90 Z" fill="var(--leaf)"/>
    <g class="massage-photo" role="img" aria-label="Photo of a man in a sports helmet lying face down on a towel while receiving a back massage">
      <rect x="0" y="560" width="873" height="640" fill="url(#photo-tone)"/>
      <rect x="0" y="560" width="873" height="640" fill="url(#photo-fade)"/>
    </g>
    <path class="band-swoosh" d="M0 664 Q420 760 873 445 L873 530 Q430 820 0 698 Z" fill="var(--leaf)"/>
  </svg>

  <header class="brand">
    <h1 class="brand-name">Sorevo massage</h1>
    <p class="brand-tagline">Relax Renew Revive</p>
  </header>

  <section class="contacts">
    <svg class="phone-icon" viewBox="0 0 44 78" aria-hidden="true">
      <rect x="2" y="2" width="40" height="74" rx="5" fill="none" stroke="var(--leaf)" stroke-width="3"/>
      <line x1="2" y1="12" x2="42" y2="12" stroke="var(--leaf)" stroke-width="2"/>
      <line x1="2" y1="64" x2="42" y2="64" stroke="var(--leaf)" stroke-width="2"/>
      <circle cx="22" cy="70" r="2.5" fill="var(--leaf)"/>
    </svg>
    <div class="location">
      <p class="location-phone">0882719064</p>
      <p class="location-detail">Location Brinkley Lane Medical Clinic<br>for an appointment</p>
    </div>
    <div class="location">
      <p class="location-phone">0886217359</p>
      <p class="location-detail">Location uHealth on Torvale<br>for an appointment</p>
    </div>
  </section>

  <p class="services">
    <span class="services-line">Deep tissue</span>
    <span class="services-line services-line--lead">Sports massage</span>
  </p>
</main>
</body>
</html>
```